SOC audit and security advisory company

We are a small public accounting firm that specializes in SOC attestations for small to medium sized business throughout the U.S. Our business is much like consulting, but we form an opinion about their operational controls. We are looking for "relevance and with a hint of polished sophistication". Our logo colors are dark gray and red. Our existing site is www.tolvanpartners.com for detailed information. We would like to include some type of captcha if possible. This is an information only site.

Target Market(s)

Small to medium sized financial and IT audit companies that are innovative and flexible.

Industry/Entity Type

Auditing

Coding

Coded - Design and coding required

Number of Pages Required

4 page

Font styles to use
Sans Serif

Requirements
Must have
• Good flow and attention to the content.
Nice to have
• CAPTCHA for contact us page
Should not have
• Big Bold lines.
• Too many distractions.

```html
<!DOCTYPE html>
<html lang="en">
<head>
<meta charset="utf-8">
<title>Tolvan Audit &amp; Advisory</title>
<link href="https://fonts.googleapis.com/css2?family=Questrial&display=swap" rel="stylesheet">
<style>
:root{
  --red:#cc0000;
  --dark:#222222;
  --darker:#111111;
  --text:#555555;
  --heading:#444444;
  --light:#f2f2f2;
  --band:#8e8e8e;
  --white:#ffffff;
}
*{margin:0;padding:0;box-sizing:border-box}
html,body{width:928px;height:1200px;overflow:hidden;background:var(--white)}
body{font-family:"Questrial",sans-serif;color:var(--text);position:relative}
.abs{position:absolute}
.header .brand{left:161px;top:14px;font-size:24px;color:var(--heading);letter-spacing:1px}
.header .brand small{display:block;font-size:6px;color:var(--red);letter-spacing:1px;margin-top:-2px}
.header .email{right:162px;top:13px;font-size:10px;color:#666;display:flex;align-items:center;gap:8px}
.header .call{right:162px;top:34px;display:flex;align-items:center;gap:6px;font-size:13px;color:#777}
.header .call .num{font-size:11px;color:#666}
.btn-outline{border:1px solid #333;border-radius:12px;padding:4px 10px;font-size:8px;color:#333;margin-left:8px}
.nav{left:161px;top:60px;width:605px;height:24px;background:#f4f4f4;border-top:1px solid #ddd;display:flex;font-size:7.5px;color:#444}
.nav a{display:flex;align-items:center;padding:0 22px;text-decoration:none;color:inherit}
.nav a.active{background:var(--red);color:var(--white);padding:0 26px}
.hero{left:161px;top:84px;width:605px;height:234px;background:linear-gradient(180deg,#2c2c2c,#1b1b1b);overflow:hidden}
.hero .accent{left:0;top:116px;width:0;height:0;border-bottom:118px solid #8a0000;border-right:150px solid transparent}
.hero .photo{right:20px;top:10px;width:170px;height:224px;background:linear-gradient(180deg,#d8c3b0,#9fb3cc 45%,#8aa0bc);border-radius:60px 60px 0 0}
.hero .caption{left:42px;top:20px;width:349px;height:90px;background:rgba(60,60,60,.85);padding:16px 34px}
.hero h1{font-weight:400;font-size:16.5px;color:var(--white);line-height:18px;letter-spacing:.5px}
.hero p{font-size:7.5px;color:#eee;line-height:11px;margin-top:9px}
.who{left:0;top:318px;width:928px;height:166px;background:var(--light);text-align:center}
.who h2{font-weight:400;font-size:13px;color:var(--heading);margin-top:27px;letter-spacing:.5px}
.who p{font-size:7.2px;line-height:11px;width:470px;margin:8px auto 0}
.who p+p{margin-top:4px;width:420px}
.btn-dark{display:inline-block;background:#555;color:#fff;font-size:7.5px;padding:5px 12px;border-radius:10px;margin-top:19px}
.slider{left:427px;top:309px;width:75px;height:18px;background:#555;border-radius:9px;display:flex;align-items:center;justify-content:space-between;padding:0 9px;color:#fff;font-size:10px;z-index:3}
.slider i{display:inline-block;width:5px;height:5px;border-radius:50%;background:#fff;margin:0 2px;vertical-align:middle}
.slider i.on{background:var(--red)}
.services-title{left:161px;top:503px;font-size:13px;color:var(--heading);letter-spacing:.5px}
.band{left:0;top:674px;width:928px;height:128px;background:var(--band)}
.svc{top:542px;width:128px;color:#fff;z-index:2}
.svc .title{position:absolute;top:151px;font-size:9px;color:#222;line-height:11px;letter-spacing:.3px;width:140px}
.svc .desc{position:absolute;top:180px;font-size:7px;line-height:11px;color:#f2f2f2;width:128px}
.person{left:602px;top:548px;width:164px;height:254px;background:linear-gradient(180deg,#e0c7b2 0,#d9bca6 30%,#2f3f66 45%,#223056 100%);border-radius:70px 70px 0 0}
.col h3{font-weight:400;font-size:13px;color:var(--heading);letter-spacing:.5px}
.col p{font-size:7.2px;line-height:11px;margin-top:8px}
.col ul{list-style:none;font-size:7.2px;line-height:11px;margin-top:6px}
.col li::before{content:"› "}
.divider{left:432px;top:832px;width:1px;height:160px;background:#ddd}
.cta{left:0;top:1022px;width:928px;height:41px;background:var(--red);color:#fff}
.cta h4{position:absolute;left:161px;top:6px;font-weight:400;font-size:15px}
.cta p{position:absolute;left:161px;top:24px;font-size:7.2px}
.cta .btn{position:absolute;left:694px;top:11px;background:#111;color:#fff;font-size:7.5px;padding:5px 16px;border-radius:10px}
.footer{left:0;top:1063px;width:928px;height:113px;background:var(--dark);color:#ddd;text-align:center}
.fcol{position:absolute;top:0;height:113px}
.fcol h5{font-weight:400;font-size:12px;color:#eee;margin-top:20px}
.fcol p{font-size:7.2px;line-height:11.5px;margin-top:6px}
.fcol+.fcol{border-left:1px solid #3a3a3a}
.social{display:flex;gap:6px;justify-content:center;margin-top:8px}
.social span{width:13px;height:13px;background:#eee}
.social span.on{background:var(--red)}
.bottom{left:0;top:1176px;width:928px;height:24px;background:var(--darker);font-size:7px;color:#ccc}
.bottom .links{position:absolute;left:160px;top:8px}
.bottom .copy{position:absolute;right:170px;top:8px}
</style>
</head>
<body>
<header class="header">
  <div class="abs brand">TOLVAN<small>AUDIT &amp; ADVISORY</small></div>
  <div class="abs email">
    <svg width="12" height="9" viewBox="0 0 12 9"><rect x=".5" y=".5" width="11" height="8" fill="none" stroke="#777"/><path d="M.5 .5 6 5 11.5 .5" fill="none" stroke="#777"/></svg>
    hello@tolvanpartners.com
  </div>
  <div class="abs call">Free Consultation
    <svg width="12" height="10" viewBox="0 0 12 10"><path d="M1 3C1 1 3 0 6 0s5 1 5 3H8V2H4v1z M3 4h6l2 6H1z" fill="#cc0000"/></svg>
    <span class="num">+1.727.555.0148</span>
    <span class="btn-outline">Contact Now</span>
  </div>
</header>
<nav class="abs nav">
  <a class="active">Home</a><a>SOC and Advisory Services</a><a>About Us</a><a>Contact Us</a>
</nav>
<section class="abs hero">
  <div class="abs accent"></div>
  <div class="abs photo" role="img" aria-label="Smiling consultant in shirt and tie holding a tablet with charts"></div>
  <div class="abs caption">
    <h1>Over 35 years experience in audit and advisory services.</h1>
    <p>When you are ready to take that next step, we are there to keeep you on the right path.</p>
  </div>
</section>
<section class="abs who">
  <h2>Who We Are</h2>
  <p>Our team is made up of seasoned professionals with backgrounds in regulatory compliance, IT audit, financial audit, and IT professional services. Our prinicpal directive is to deliver high quality services to a reduced client base, where a client becomes a relationship, not a number.</p>
  <p>- We thank you for your interest in Tolvan Audit &amp; Advisory Services. Contact us to find out more about why we are the right audit and compliance choice for your organization.</p>
  <span class="btn-dark">Read More...</span>
</section>
<div class="abs slider"><span>‹</span><span><i></i><i class="on"></i><i></i></span><span>›</span></div>
<h2 class="abs services-title" style="font-weight:400">Professional Advisory services</h2>
<div class="abs band"></div>
<div class="abs person" role="img" aria-label="Smiling businessman in a navy suit giving a thumbs up"></div>
<svg class="abs" style="left:0;top:540px" width="600" height="150" viewBox="0 540 600 150">
  <g>
    <circle cx="230" cy="572" r="30" fill="#cc0000"/><path d="M230 602l-6-6h12z" fill="#cc0000"/>
    <path d="M230 557v28M220 585h20M214 563h32M214 563l-5 11h10zM246 563l-5 11h10z" stroke="#fff" stroke-width="1.6" fill="none"/>
    <line x1="230" y1="606" x2="230" y2="664" stroke="#cc0000" stroke-dasharray="2 2"/>
    <rect x="223" y="667" width="14" height="14" transform="rotate(45 230 674)" fill="#cc0000"/>
    <text x="230" y="677" font-size="8" fill="#fff" text-anchor="middle" font-family="Questrial,sans-serif">1</text>
  </g>
  <g>
    <circle cx="386" cy="572" r="30" fill="#dedede"/><path d="M386 602l-6-6h12z" fill="#dedede"/>
    <path d="M380 570v-5a6 6 0 0 1 12 0v5" stroke="#cc0000" stroke-width="2.4" fill="none"/>
    <rect x="376" y="569" width="20" height="15" fill="#cc0000"/><circle cx="386" cy="576" r="2" fill="#fff"/>
    <line x1="386" y1="606" x2="386" y2="664" stroke="#ccc" stroke-dasharray="2 2"/>
    <rect x="379" y="667" width="14" height="14" transform="rotate(45 386 674)" fill="#dedede"/>
    <text x="386" y="677" font-size="8" fill="#666" text-anchor="middle" font-family="Questrial,sans-serif">2</text>
  </g>
  <g>
    <circle cx="542" cy="572" r="30" fill="#cc0000"/><path d="M542 602l-6-6h12z" fill="#cc0000"/>
    <rect x="530" y="560" width="22" height="24" rx="2" stroke="#fff" stroke-width="1.6" fill="none"/>
    <rect x="537" y="570" width="11" height="9" fill="#fff"/><path d="M539 570v-3a3 3 0 0 1 7 0v3" stroke="#fff" stroke-width="1.4" fill="none"/>
    <line x1="542" y1="606" x2="542" y2="664" stroke="#cc0000" stroke-dasharray="2 2"/>
    <rect x="535" y="667" width="14" height="14" transform="rotate(45 542 674)" fill="#cc0000"/>
    <text x="542" y="677" font-size="8" fill="#fff" text-anchor="middle" font-family="Questrial,sans-serif">3</text>
  </g>
</svg>
<div class="abs svc" style="left:161px"><div class="title">Consumer Financial<br>Protection Bureau (CFPB)</div><div class="desc">As a result of Wall Street reform, companies who are consumer facing must meet a minimum federally regulated posture.</div></div>
<div class="abs svc" style="left:317px"><div class="title">HIPAA Security<br>Assessments</div><div class="desc">Our staff of certified HIPAA professionals can help to identify and close those gaps that pose threats to your business model.</div></div>
<div class="abs svc" style="left:473px"><div class="title">IT Security<br>Reviews</div><div class="desc">A "perimeter in" review is conducted based on COSO, CoBIT, ISACA and ISO frameworks. Our staff consists of certified.</div></div>
<section class="abs col" style="left:161px;top:827px;width:250px">
  <h3>Why Tolvan?</h3>
  <p>Our proven implementation and audit models allow for capturing requirements while expiditing the process.</p>
  <ul><li>Free consultation</li><li>Fixed cost</li><li>Results driven</li></ul>
  <p>Our professionals maintain certifications required for your service needs. We utilize the best so you get the best results.</p>
  <ul><li>CPA</li><li>CHP</li><li>CISA</li><li>CISSP</li><li>ISO/IEC 27001</li></ul>
</section>
<div class="abs divider"></div>
<section class="abs col" style="left:472px;top:827px;width:250px">
  <h3>Contact Us Today!</h3>
  <p>Whether you are fact finding or ready to make a decsion, we are happy to answer any questions you may have. Contact us today and find out why Tolvan is the right fit for you.</p>
  <p style="margin-top:3px">We are happy to provide you with information on the following services:</p>
  <ul><li>SOC 1</li><li>SOC 2</li><li>CFPB Professional Services</li><li>ISO 27002 Professional Services</li><li>HIPAA Security Review</li><li>IT Security Review</li></ul>
</section>
<section class="abs cta">
  <h4>Need More Details? Contact us</h4>
  <p>We are here to assist. Contact us by phone, email or via our social media channels.</p>
  <span class="btn">Contact Us</span>
</section>
<footer class="abs footer">
  <div class="fcol" style="left:161px;width:162px"><h5>Home Address</h5><p><b>Tolvan Audit &amp; Advisory, Inc</b><br>418 Harbor Street North<br>Suite 210<br>Clearwater, FL 33755<br>United States</p></div>
  <div class="fcol" style="left:323px;width:135px"><h5>Call</h5><p>+17275550192<br>+17275550137</p></div>
  <div class="fcol" style="left:458px;width:159px"><h5>Contact Us</h5><p>office@tolvanpartners.com<br>audit@tolvanpartners.com</p></div>
  <div class="fcol" style="left:617px;width:160px"><h5>Social Media</h5><div class="social"><span></span><span></span><span class="on"></span><span></span><span></span></div></div>
</footer>
<div class="abs bottom">
  <span class="links">Home &nbsp;/&nbsp; SOC and Advisory Services &nbsp;/&nbsp; About Us &nbsp;/&nbsp; Contact Us</span>
  <span class="copy">Copyright 2016 Tolvan Audit &amp; Advisory, Inc. All rights reserved.</span>
</div>
</body>
</html>
```